Business Card Design Project

we need a business card design for our company: www.plomvik.ch
It's important to include our already existing logo (see website)

```html
<!DOCTYPE html>
<html lang="en">
<head>
<meta charset="utf-8">
<title>Plomvik business card</title>
<link rel="stylesheet" href="https://fonts.googleapis.com/css2?family=PT+Sans:wght@400;700&display=swap">
<style>
  :root {
    --page-bg: #e4e4e6;
    --card-white: #ffffff;
    --card-black: #0e0b0d;
    --brand-blue: #1b7bc4;
    --band-blue: #1a78c2;
    --url-blue: #7fb6e6;
    --name-band: #eeeeef;
    --text-grey: #7a7a7a;
    --text-dark: #2a2a2a;
    --card-edge: #d2d2d4;
  }
  * { box-sizing: border-box; margin: 0; padding: 0; }
  html, body {
    width: 1168px; height: 1200px; overflow: hidden;
    background: var(--page-bg);
    font-family: "PT Sans", Arial, sans-serif;
  }
  .canvas { position: relative; width: 1168px; height: 1200px; }

  .card {
    position: absolute;
    width: 582px; height: 356px;
    overflow: hidden;
  }
  .card--front { left: 121px; top: 224px; background: var(--card-white); border: 1px solid var(--card-edge); }
  .card--back  { left: 499px; top: 620px; background: var(--card-black); }

  .brand { position: absolute; display: flex; flex-direction: column; }
  .brand__name {
    display: flex; align-items: center; gap: 12px;
    font-size: 62px; font-weight: 700; line-height: 1;
    color: var(--brand-blue); letter-spacing: -0.5px;
  }
  .brand__mark { width: 34px; height: 34px; background: var(--brand-blue); }
  .brand__tagline {
    font-size: 14px; letter-spacing: 0.3px; margin-top: 8px;
    color: var(--text-dark); padding-left: 92px;
  }
  .card--front .brand { left: 30px; top: 38px; }
  .card--back .brand { left: 136px; top: 130px; }
  .card--back .brand__tagline { color: #d8d8d8; }

  .name-band {
    position: absolute; left: 124px; right: 0; top: 157px; height: 36px;
    background: var(--name-band);
    display: flex; align-items: center; padding-left: 4px;
  }
  .person__name { font-size: 22px; color: var(--brand-blue); letter-spacing: 0.3px; }
  .person__role { font-size: 18px; color: var(--text-dark); margin-left: 6px; }

  .address {
    position: absolute; left: 128px; top: 200px;
    font-size: 18px; line-height: 22px; color: var(--text-grey); font-style: normal;
  }
  .contacts {
    position: absolute; left: 128px; top: 259px; list-style: none;
    font-size: 18px; line-height: 22.5px; color: var(--text-dark);
  }
  .contacts__key { display: inline-block; width: 22px; font-weight: 700; color: var(--brand-blue); }

  .band { position: absolute; left: 0; right: 0; bottom: 0; background: var(--band-blue); }
  .card--front .band { height: 26px; }
  .card--back .band {
    height: 28px; display: flex; align-items: center; justify-content: center;
    font-size: 16px; color: var(--url-blue);
  }
</style>
</head>
<body>
<main class="canvas">
  <section class="card card--front" aria-label="Business card front">
    <div class="brand">
      <div class="brand__name"><span class="brand__mark"></span>Plomvik</div>
      <div class="brand__tagline">BUSINESS SOFTWARE GROUP</div>
    </div>
    <div class="name-band">
      <span class="person__name">LENZ MARTI</span>
      <span class="person__role">- Director</span>
    </div>
    <address class="address">Lindenweg 12<br>8005 Zürich</address>
    <ul class="contacts">
      <li><span class="contacts__key">P</span>: +41 44 000 12 34</li>
      <li><span class="contacts__key">E</span>: info@plomvik.ch</li>
      <li><span class="contacts__key">W</span>: www.plomvik.ch</li>
    </ul>
    <div class="band"></div>
  </section>

  <section class="card card--back" aria-label="Business card back">
    <div class="brand">
      <div class="brand__name"><span class="brand__mark"></span>Plomvik</div>
      <div class="brand__tagline">BUSINESS SOFTWARE GROUP</div>
    </div>
    <div class="band">www.plomvik.ch</div>
  </section>
</main>
</body>
</html>
```